Business card design for event company

need design double sided in square shape ( approx 6x6cm) in matt grey shades
front side :
logo ( could be in one color like picture attached ) printpress effect in a rect box

back side :
name in big font with silver foil finish ( similar to attached pic )

phone number i would like to see how it will look like if embossed ( like in credit cards )

Sample for contact on card ( will need 5 different contacts) - pls. include small icons next to each contact

WALEED RAFIQI
Managing Director

+971 50 317 6490
waleed@loomcrestuae.com
www.loomcrest.ae
Building C2 , Office 713
Dubai Saffron Heights

Please consider this is an urgent project . thank you in advance

```html
<!DOCTYPE html>
<html lang="en">
<head>
<meta charset="utf-8">
<title>Loomcrest Business Card</title>
<link href="https://fonts.googleapis.com/css2?family=Roboto:wght@100;300;400;500;700&display=swap" rel="stylesheet">
<style>
  :root {
    --backdrop: #2b2c2e;
    --card-grey: #6f747b;
    --ink-light: #dcdde0;
    --ink-foil: #e4e5e8;
    --ink-soft: #c9cbcf;
    --rule: #c3c5c9;
    --shadow-dark: rgba(0,0,0,0.45);
  }
  * { margin: 0; padding: 0; box-sizing: border-box; }
  html, body {
    width: 1200px; height: 1000px; overflow: hidden;
    background: var(--backdrop);
    font-family: "Roboto", Arial, sans-serif;
  }
  .canvas { position: relative; width: 1200px; height: 1000px; }

  .card {
    position: absolute;
    width: 460px; height: 460px;
    background: var(--card-grey);
    box-shadow: 0 10px 24px var(--shadow-dark);
  }
  .card--front { left: 370px; top: 22px; }
  .card--back  { left: 370px; top: 512px; padding: 58px 52px 0 52px; }

  /* front */
  .brand-name {
    position: absolute; left: 0; right: 0; top: 196px;
    text-align: center;
    font-size: 56px; font-weight: 500; letter-spacing: 1px;
    color: var(--ink-light);
    text-shadow: 0 -1px 0 rgba(0,0,0,0.35), 0 1px 0 rgba(255,255,255,0.15);
  }

  /* back */
  .person-first {
    font-size: 58px; font-weight: 100; line-height: 0.95;
    color: var(--ink-foil); letter-spacing: 0.5px;
  }
  .person-last {
    font-size: 58px; font-weight: 700; line-height: 0.95;
    color: var(--ink-foil); letter-spacing: 0.5px;
  }
  .person-role {
    margin-top: 8px;
    font-size: 15px; font-weight: 400; letter-spacing: 4.6px;
    color: var(--ink-soft);
  }
  .rule { height: 1px; background: var(--rule); margin: 14px 0 10px; width: 340px; }
  .contact-list { list-style: none; }
  .contact-item {
    display: flex; align-items: flex-start; gap: 8px;
    font-size: 16px; color: var(--ink-light); line-height: 1.35;
    margin-bottom: 3px;
  }
  .contact-item--web { letter-spacing: 3.6px; }
  .contact-icon { width: 16px; height: 16px; flex: none; margin-top: 3px; }
  .address { display: block; }
  .phone-embossed {
    display: flex; align-items: center; gap: 8px;
    font-size: 24px; font-weight: 500; letter-spacing: 3px;
    color: #e6e7ea;
    text-shadow: 1px 1px 0 rgba(0,0,0,0.45), -1px -1px 0 rgba(255,255,255,0.25);
  }
  .phone-embossed .contact-icon { width: 22px; height: 22px; margin-top: 0; }
</style>
</head>
<body>
<div class="canvas">

  <section class="card card--front">
    <div class="brand-name">Loomcrest</div>
  </section>

  <section class="card card--back">
    <div class="person-first">WALEED</div>
    <div class="person-last">RAFIQI</div>
    <div class="person-role">MANAGING DIRECTOR</div>
    <div class="rule"></div>
    <ul class="contact-list">
      <li class="contact-item">
        <svg class="contact-icon" viewBox="0 0 16 16"><circle cx="8" cy="8" r="8" fill="#d8d9dc"/><rect x="4" y="5" width="8" height="6" fill="none" stroke="#6f747b" stroke-width="1.2"/><path d="M4 5l4 3 4-3" fill="none" stroke="#6f747b" stroke-width="1.2"/></svg>
        <span>waleed@loomcrestuae.com</span>
      </li>
      <li class="contact-item contact-item--web">
        <svg class="contact-icon" viewBox="0 0 16 16"><circle cx="8" cy="8" r="8" fill="#d8d9dc"/><circle cx="8" cy="8" r="4.5" fill="none" stroke="#6f747b" stroke-width="1.1"/><path d="M3.5 8h9M8 3.5c-2 2.5-2 6.5 0 9M8 3.5c2 2.5 2 6.5 0 9" fill="none" stroke="#6f747b" stroke-width="1"/></svg>
        <span>www.loomcrest.ae</span>
      </li>
      <li class="contact-item">
        <svg class="contact-icon" viewBox="0 0 16 16"><circle cx="8" cy="8" r="8" fill="#d8d9dc"/><path d="M8 13s-3.5-3.8-3.5-6.2a3.5 3.5 0 0 1 7 0C11.5 9.2 8 13 8 13z" fill="#6f747b"/><circle cx="8" cy="6.8" r="1.3" fill="#d8d9dc"/></svg>
        <span class="address">Building C2 , Office 713<br>Dubai Saffron Heights</span>
      </li>
    </ul>
    <div class="rule"></div>
    <div class="phone-embossed">
      <svg class="contact-icon" viewBox="0 0 16 16"><circle cx="8" cy="8" r="8" fill="#d8d9dc"/><path d="M5.2 4.2l1.6-.4 1 2.2-1 .8a6 6 0 0 0 2.4 2.4l.8-1 2.2 1-.4 1.6c-3.6.4-7-3-6.6-6.6z" fill="#6f747b"/></svg>
      <span>+971 50 317 6490</span>
    </div>
  </section>

</div>
</body>
</html>
```